Business Card design for shipping company 'FERNHOLT INTERNATIONAL LTD'

Classic / traditional business card in black Garamond / Times New Roman or similar text for a shipping / marine transport company, containing the following information:

QUOTE

FERNHOLT INTERNATIONAL LTD

MARTIN QUESTEDGE FICS

T: +44 7902 615370
E: cargo@fernholt-example.com

UNQUOTE

Target Market(s)

Marine / Shipping industry

Contact Information for Business Card

FERNHOLT INTERNATIONAL LTD MARTIN QUESTEDGE FICS T: +44 7902 615370 E: cargo@fernholt-example.com

Font styles to use
Serif

Colors

Designer to choose colors to be used in the design.

Requirements
Must have
• Garamond / Times New Roman or similar text in black colour

```html
<!DOCTYPE html>
<html lang="en">
<head>
<meta charset="utf-8">
<title>Fernholt International Ltd – Business Card</title>
<link rel="stylesheet" href="https://fonts.googleapis.com/css2?family=EB+Garamond:wght@400;600&display=swap">
<style>
  :root {
    --backdrop: #d1d0d1;
    --card: #4d4e4e;
    --ink: #ffffff;
    --ink-soft: #c9caca;
    --rule: #8d8e8e;
    --shadow: rgba(0, 0, 0, 0.28);
  }
  * { margin: 0; padding: 0; box-sizing: border-box; }
  html, body {
    width: 1200px;
    height: 900px;
    overflow: hidden;
    background: var(--backdrop);
  }
  .canvas {
    position: relative;
    width: 1200px;
    height: 900px;
    font-family: "EB Garamond", "Times New Roman", serif;
    color: var(--ink);
  }
  .card {
    position: absolute;
    width: 560px;
    height: 320px;
    background: var(--card);
    box-shadow: 0 6px 14px var(--shadow);
  }
  .card--front { left: 250px; top: 110px; }
  .card--back  { left: 390px; top: 470px; }

  .wordmark {
    font-weight: 600;
    letter-spacing: 0.06em;
    line-height: 1.05;
    color: var(--ink);
    text-transform: uppercase;
  }
  .wordmark__main { display: block; font-size: 34px; }
  .wordmark__sub  { display: block; font-size: 17px; letter-spacing: 0.14em; }

  .card--front .wordmark {
    position: absolute;
    left: 50%;
    top: 50%;
    transform: translate(-50%, -50%);
    text-align: center;
  }

  .card--back .wordmark {
    position: absolute;
    right: 36px;
    top: 34px;
    text-align: right;
  }
  .back__rule {
    position: absolute;
    left: 236px;
    right: 0;
    top: 118px;
    height: 1px;
    background: var(--rule);
  }

  .holder {
    position: absolute;
    left: 36px;
    top: 168px;
  }
  .holder__name {
    font-size: 19px;
    font-weight: 600;
    letter-spacing: 0.03em;
    text-transform: uppercase;
  }
  .holder__title {
    font-size: 14px;
    color: var(--ink-soft);
    letter-spacing: 0.04em;
    padding-bottom: 6px;
    border-bottom: 1px solid var(--rule);
    width: 300px;
  }

  .contacts {
    position: absolute;
    left: 36px;
    top: 232px;
    list-style: none;
  }
  .contacts__item {
    display: flex;
    align-items: flex-start;
    gap: 10px;
    font-size: 15px;
    letter-spacing: 0.05em;
    line-height: 18px;
    margin-bottom: 6px;
  }
  .contacts__icon { width: 18px; height: 18px; flex: none; }
</style>
</head>
<body>
<main class="canvas">

  <section class="card card--front" aria-label="Card front">
    <div class="wordmark">
      <span class="wordmark__main">Fernholt</span>
      <span class="wordmark__sub">International Ltd</span>
    </div>
  </section>

  <section class="card card--back" aria-label="Card back">
    <div class="wordmark">
      <span class="wordmark__main">Fernholt</span>
      <span class="wordmark__sub">International Ltd</span>
    </div>
    <div class="back__rule"></div>

    <div class="holder">
      <p class="holder__name">Martin Questedge FICS</p>
      <p class="holder__title">Managing Director</p>
    </div>

    <ul class="contacts">
      <li class="contacts__item">
        <svg class="contacts__icon" viewBox="0 0 18 18" aria-hidden="true">
          <circle cx="9" cy="9" r="9" fill="#ffffff"/>
          <path d="M6 4.5 L7.6 4.5 L8.2 7 L7.2 7.8 Q8 9.8 10.2 10.8 L11 9.8 L13.5 10.4 L13.5 12 Q13 13.5 11.2 13.3 Q5 12 4.7 6.2 Q4.6 4.6 6 4.5 Z" fill="#4d4e4e"/>
        </svg>
        <span>+44 7902 615370</span>
      </li>
      <li class="contacts__item">
        <svg class="contacts__icon" viewBox="0 0 18 18" aria-hidden="true">
          <circle cx="9" cy="9" r="9" fill="#ffffff"/>
          <rect x="4.5" y="5.8" width="9" height="6.4" fill="none" stroke="#4d4e4e" stroke-width="1.2"/>
          <path d="M4.5 5.8 L9 9.4 L13.5 5.8" fill="none" stroke="#4d4e4e" stroke-width="1.2"/>
        </svg>
        <span>cargo@fernholt-example.com</span>
      </li>
      <li class="contacts__item">
        <svg class="contacts__icon" viewBox="0 0 18 18" aria-hidden="true">
          <circle cx="9" cy="9" r="9" fill="#ffffff"/>
          <path d="M9 14.2 Q5.4 10 5.4 7.6 A3.6 3.6 0 0 1 12.6 7.6 Q12.6 10 9 14.2 Z" fill="#4d4e4e"/>
          <circle cx="9" cy="7.6" r="1.4" fill="#ffffff"/>
        </svg>
        <span>123 Anywhere St., Any City,<br>ST 12345</span>
      </li>
    </ul>
  </section>

</main>
</body>
</html>
```